Marbury 720 - Strategic Planning Consulting - Business Card Design

We need a business card design for a national public affairs consulting firm. We specialize in strategic planning for non-profit organizations including designing winning advocacy and communications campaigns. I'd like the design to be fresh and use the logo colors and the card should have rounded edges. On the back of the card I'd like a few words that help folks understand our services:

Strategic Planning
Advocacy Campaigns
Communications
Updates

Thank you to all the designers for your amazing work.  I wish I could select all of your talented designs.

Target Market(s)

The target customer is a CEO or VP of Public Policy or Communications.

Industry/Entity Type

Communications

Requirements
Must have
• Include:

LOGO

Loretta K. Vanhorn
President/CEO

4853 SE 17th Lane
Boca Raton, FL 33428

561.374.2096

Loretta@Marbury720.com
www.Marbury720.com

On back of card:
Strategic Planning
Advocacy Campaigns
Communications

```html
<!DOCTYPE html>
<html lang="en">
<head>
<meta charset="utf-8">
<title>Marbury 720 – Business Card</title>
<link rel="stylesheet" href="https://fonts.googleapis.com/css2?family=Open+Sans:wght@400;600&family=Ubuntu:wght@500;700&display=swap">
<style>
  :root {
    --purple: #8a55a6;
    --grey: #6b6c6e;
    --grey-dark: #58595b;
    --ink: #333335;
    --muted: #77787a;
    --paper: #ffffff;
    --backdrop: #ececec;
    --rule: #c9c9c9;
    --sheen: #cfcfd0;
  }
  * { box-sizing: border-box; margin: 0; padding: 0; }
  html, body {
    width: 1200px; height: 1023px; overflow: hidden;
    background: var(--backdrop);
    font-family: "Open Sans", Arial, sans-serif;
  }
  .card {
    position: absolute; left: 220px;
    width: 760px; height: 434px;
    border-radius: 34px; overflow: hidden;
    box-shadow: 0 6px 18px rgba(0,0,0,.18);
  }
  .swoosh { position: absolute; left: 0; bottom: 0; width: 760px; height: 434px; }

  .brand-name { font-family: "Ubuntu", sans-serif; font-weight: 700; font-size: 70px; line-height: 1; letter-spacing: -1px; white-space: nowrap; }
  .tagline { font-family: "Open Sans", sans-serif; font-weight: 600; font-size: 17px; margin-top: 8px; white-space: nowrap; }

  /* Back */
  .card-back { top: 48px; background: var(--grey); }
  .card-back .brand { position: absolute; top: 120px; width: 100%; text-align: center; color: var(--paper); }
  .services {
    position: absolute; left: 0; right: 0; bottom: 22px;
    display: flex; justify-content: center; align-items: center; gap: 14px;
    color: var(--paper); font-size: 18px; white-space: nowrap;
  }
  .services .dot { width: 8px; height: 8px; border: 2px solid var(--paper); border-radius: 50%; }

  /* Front */
  .card-front { top: 540px; background: var(--paper); }
  .card-front .brand { position: absolute; top: 48px; left: 34px; }
  .card-front .brand-name { color: var(--purple); font-size: 64px; }
  .card-front .tagline { color: var(--grey-dark); font-size: 16px; margin-top: 6px; }
  .person { position: absolute; top: 146px; right: 40px; text-align: right; }
  .person-name { font-family: "Ubuntu", sans-serif; font-weight: 500; font-size: 26px; color: var(--purple); white-space: nowrap; }
  .person-title { font-size: 18px; color: var(--muted); }
  .divider { position: absolute; top: 210px; left: 30px; width: 540px; height: 1px; background: var(--rule); }
  .address { position: absolute; top: 232px; left: 30px; font-size: 18px; line-height: 24px; color: var(--ink); font-style: normal; }
  .contacts { position: absolute; top: 300px; left: 30px; list-style: none; font-size: 18px; color: var(--ink); }
  .contacts li { display: flex; align-items: center; gap: 10px; height: 26px; white-space: nowrap; }
  .contacts svg { width: 20px; height: 20px; flex: none; }
</style>
</head>
<body>

<section class="card card-back" aria-label="Card back">
  <div class="brand">
    <div class="brand-name">Marbury 720</div>
    <div class="tagline">Guiding Vision and Public Voice</div>
  </div>
  <svg class="swoosh" viewBox="0 0 760 434" aria-hidden="true">
    <path d="M0 360 C260 350 560 300 760 232 L760 434 L0 434 Z" fill="var(--sheen)"/>
    <path d="M0 366 C260 356 560 308 760 242 L760 434 L0 434 Z" fill="var(--purple)"/>
  </svg>
  <div class="services">
    <span>Strategic Planning</span><span class="dot"></span>
    <span>Advocacy Campaigns</span><span class="dot"></span>
    <span>Communications</span>
  </div>
</section>

<section class="card card-front" aria-label="Card front">
  <div class="brand">
    <div class="brand-name">Marbury 720</div>
    <div class="tagline">Guiding Vision and Public Voice</div>
  </div>
  <div class="person">
    <div class="person-name">Loretta K. Vanhorn</div>
    <div class="person-title">President/CEO</div>
  </div>
  <div class="divider"></div>
  <address class="address">
    4853 SE 17th Lane<br>Boca Raton, FL 33428
  </address>
  <ul class="contacts">
    <li><svg viewBox="0 0 20 20" aria-hidden="true"><circle cx="10" cy="10" r="10" fill="var(--purple)"/><rect x="7" y="4.5" width="6" height="11" rx="1.2" fill="none" stroke="#fff" stroke-width="1.4"/></svg>561.374.2096</li>
    <li><svg viewBox="0 0 20 20" aria-hidden="true"><circle cx="10" cy="10" r="10" fill="var(--purple)"/><rect x="5" y="6.5" width="10" height="7" fill="none" stroke="#fff" stroke-width="1.3"/><path d="M5 6.5 L10 11 L15 6.5" fill="none" stroke="#fff" stroke-width="1.3"/></svg>Loretta@Marbury720.com</li>
    <li><svg viewBox="0 0 20 20" aria-hidden="true"><circle cx="10" cy="10" r="10" fill="var(--purple)"/><circle cx="10" cy="10" r="5.5" fill="none" stroke="#fff" stroke-width="1.2"/><ellipse cx="10" cy="10" rx="2.4" ry="5.5" fill="none" stroke="#fff" stroke-width="1.1"/><path d="M4.5 10 H15.5" stroke="#fff" stroke-width="1.1"/></svg>www.Marbury720.com</li>
  </ul>
  <svg class="swoosh" viewBox="0 0 760 434" aria-hidden="true">
    <path d="M320 384 C520 370 670 340 760 300 L760 330 C640 360 490 378 320 384 Z" fill="var(--grey)"/>
    <path d="M0 410 C300 404 560 384 760 334 L760 434 L0 434 Z" fill="var(--purple)"/>
    <path d="M0 410 C300 404 560 384 760 334" fill="none" stroke="#fff" stroke-width="3"/>
  </svg>
</section>

</body>
</html>
```